Business Card for Graphic Design Firm

This project is for a new graphic design firm based in New Jersey called Velmoth. We outsource graphic design and marketing jobs. We want to communicate that this is a professional company but it as well creative and artistic. This card may be used as a horizontal double sided paper card or a vertical single sided translucent card so feel free to submit designs in whichever format or both.
Updates

Reason: Extending the deadline because I'm not exactly satisfied with the designs so far.

Please view the updated project brief

Target Market(s)

Adults aged 25-60

Industry/Entity Type

Graphic Design

Font styles to use
Serif
Sans Serif

Requirements
Nice to have
• Maybe a triangular pattern around the edges similar to our logo

```html
<!DOCTYPE html>
<html lang="en">
<head>
<meta charset="utf-8">
<title>Velmoth Business Card</title>
<link rel="stylesheet" href="https://fonts.googleapis.com/css2?family=Open+Sans:wght@400;600;700&display=swap">
<style>
  :root {
    --backdrop: #e9e6e1;
    --card-top: #2e2e30;
    --card-bottom: #161617;
    --corner-white: #f2f2f2;
    --accent-yellow: #f2b21c;
    --text-white: #f4f4f4;
    --brand-grey: #9a9a9c;
    --brand-light: #d9d9db;
  }
  html, body {
    margin: 0;
    padding: 0;
    width: 1200px;
    height: 1023px;
    overflow: hidden;
    background: var(--backdrop);
    font-family: "Open Sans", Arial, sans-serif;
  }
  .canvas {
    position: relative;
    width: 1200px;
    height: 1023px;
  }
  .card {
    position: absolute;
    left: 220px;
    width: 760px;
    height: 434px;
    background: linear-gradient(160deg, var(--card-top), var(--card-bottom));
    box-shadow: 0 10px 28px rgba(0,0,0,0.25);
    overflow: hidden;
  }
  .card--front { top: 40px; }
  .card--back { top: 532px; }
  .card__corners {
    position: absolute;
    inset: 0;
    width: 100%;
    height: 100%;
  }
  .contact {
    position: absolute;
    left: 90px;
    top: 112px;
    color: var(--text-white);
  }
  .contact__name {
    margin: 0;
    font-size: 25px;
    font-weight: 700;
    letter-spacing: 0.2px;
  }
  .contact__role {
    margin: 2px 0 0;
    font-size: 16px;
    color: var(--accent-yellow);
  }
  .contact__list {
    list-style: none;
    margin: 26px 0 0;
    padding: 0;
  }
  .contact__item {
    display: flex;
    align-items: center;
    gap: 18px;
    margin-bottom: 22px;
    font-size: 15px;
    line-height: 1.35;
  }
  .contact__icon {
    width: 42px;
    height: 38px;
    flex: none;
  }
  .brand {
    position: absolute;
    right: 120px;
    top: 150px;
    display: flex;
    align-items: center;
    gap: 12px;
  }
  .brand__mark {
    width: 20px;
    height: 20px;
    background: var(--accent-yellow);
  }
  .brand__name {
    font-size: 30px;
    font-weight: 600;
    letter-spacing: 3px;
    color: var(--brand-light);
    text-transform: uppercase;
  }
  .brand--large {
    right: auto;
    left: 50%;
    top: 50%;
    transform: translate(-50%, -50%);
    gap: 22px;
  }
  .brand--large .brand__mark {
    width: 48px;
    height: 48px;
  }
  .brand--large .brand__name {
    font-size: 78px;
    letter-spacing: 8px;
    color: var(--brand-grey);
  }
</style>
</head>
<body>
<main class="canvas">

  <section class="card card--front" aria-label="Card front">
    <svg class="card__corners" viewBox="0 0 760 434" aria-hidden="true">
      <polygon points="0,0 62,0 0,74" fill="var(--corner-white)"/>
      <polygon points="62,0 80,0 0,96 0,74" fill="var(--accent-yellow)"/>
      <polygon points="760,434 698,434 760,360" fill="var(--corner-white)"/>
      <polygon points="698,434 680,434 760,338 760,360" fill="var(--accent-yellow)"/>
    </svg>

    <div class="contact">
      <h1 class="contact__name">Lena Hartwig</h1>
      <p class="contact__role">Hybrid Clouds</p>
      <ul class="contact__list">
        <li class="contact__item">
          <svg class="contact__icon" viewBox="0 0 42 38" aria-hidden="true">
            <polygon points="21,3 39,35 3,35" fill="none" stroke="var(--text-white)" stroke-width="2"/>
            <rect x="17" y="16" width="8" height="14" rx="1.5" fill="var(--accent-yellow)"/>
          </svg>
          <span>+41 70 555 01 23</span>
        </li>
        <li class="contact__item">
          <svg class="contact__icon" viewBox="0 0 42 38" aria-hidden="true">
            <polygon points="21,3 39,35 3,35" fill="none" stroke="var(--text-white)" stroke-width="2"/>
            <rect x="14" y="20" width="14" height="10" fill="var(--accent-yellow)"/>
            <polyline points="14,20 21,26 28,20" fill="none" stroke="#222" stroke-width="1.3"/>
          </svg>
          <span>lena@cloudrest.ch</span>
        </li>
        <li class="contact__item">
          <svg class="contact__icon" viewBox="0 0 42 38" aria-hidden="true">
            <polygon points="21,3 39,35 3,35" fill="none" stroke="var(--text-white)" stroke-width="2"/>
            <polygon points="21,16 29,23 13,23" fill="var(--accent-yellow)"/>
            <rect x="15" y="23" width="12" height="8" fill="var(--accent-yellow)"/>
          </svg>
          <span>Lindenweg 12 8400 Winterthur<br>Switzerland 8400 Winterthur, Switzerland</span>
        </li>
      </ul>
    </div>

    <div class="brand">
      <span class="brand__mark"></span>
      <span class="brand__name">Velmoth</span>
    </div>
  </section>

  <section class="card card--back" aria-label="Card back">
    <svg class="card__corners" viewBox="0 0 760 434" aria-hidden="true">
      <polygon points="0,0 62,0 0,74" fill="var(--corner-white)"/>
      <polygon points="62,0 80,0 0,96 0,74" fill="var(--accent-yellow)"/>
      <polygon points="760,434 698,434 760,360" fill="var(--corner-white)"/>
      <polygon points="698,434 680,434 760,338 760,360" fill="var(--accent-yellow)"/>
    </svg>

    <div class="brand brand--large">
      <span class="brand__mark"></span>
      <span class="brand__name">Velmoth</span>
    </div>
  </section>

</main>
</body>
</html>
```